" A maioria das empresas tem dificuldades em lidar com o quadro de funcionários. A consultoria entra fornecendo todo o suporte com treinamentos para melhoria do clima e das relações interpessoais, melhoria do atendimento ao cliente, desenvolve líderes e os capacita para lidar de maneira mais adequada com os conflitos da equipe. Além disso, também realizamos todo o processo de recrutamento e seleção. Entre outros serviços. "

```html
<!DOCTYPE html>
<html lang="pt-BR">
<head>
<meta charset="UTF-8">
<title>Ponte — Papelaria Institucional</title>
<link rel="stylesheet" href="https://fonts.googleapis.com/css2?family=Montserrat:wght@400;600;700&display=swap">
<style>
  :root {
    --backdrop: #2c2c2f;
    --paper: #ffffff;
    --paper-shade: #e6e7ea;
    --navy: #142a5c;
    --navy-deep: #0a1838;
    --amber: #e9a325;
    --ink: #3a3d44;
    --rule: #c9cbd0;
  }
  * { box-sizing: border-box; margin: 0; padding: 0; }
  html, body { width: 1200px; height: 1200px; overflow: hidden; }
  body {
    background: var(--backdrop);
    font-family: "Montserrat", sans-serif;
    position: relative;
  }
  .sheet {
    position: absolute;
    background: var(--paper);
    box-shadow: 0 6px 18px rgba(0,0,0,.35);
    overflow: hidden;
  }
  .sheet--letter-first { left: 468px; top: 151px; width: 264px; height: 432px; }
  .sheet--letter-next  { left: 283px; top: 612px; width: 305px; height: 437px; }
  .sheet--folder {
    left: 619px; top: 612px; width: 305px; height: 437px;
    background: linear-gradient(160deg, var(--navy) 0%, var(--navy-deep) 100%);
  }
  .watermark-area {
    position: absolute; z-index: 0;
    background: linear-gradient(115deg, rgba(230,231,234,0) 0%, var(--paper-shade) 45%, rgba(230,231,234,0) 100%);
  }
  .brand {
    position: absolute; z-index: 1;
    display: flex; align-items: center; gap: 5px;
  }
  .brand__mark { width: 7px; height: 7px; background: var(--amber); }
  .brand__name {
    font-weight: 700; color: var(--navy); letter-spacing: .5px; line-height: 1; font-size: 10px;
  }
  .brand__tagline {
    position: absolute; z-index: 1; font-size: 4px; color: var(--ink); white-space: nowrap;
  }
  .header-rule { position: absolute; z-index: 1; height: 1.5px; background: var(--amber); }
  .header-rule--grey { height: 1px; background: var(--rule); }
  .contact-row {
    position: absolute; left: 0; right: 0; z-index: 1;
    display: flex; justify-content: center; gap: 16px;
    font-size: 4.5px; color: var(--ink);
  }
  .contact-row__item { display: flex; align-items: center; gap: 2px; white-space: nowrap; }
  .contact-row__item svg { width: 6px; height: 6px; }
  .foot-bar {
    position: absolute; left: 50%; bottom: 0; transform: translateX(-50%);
    height: 3px; background: var(--amber);
  }
  .folder-brand { position: absolute; left: 28px; top: 205px; z-index: 1; }
  .folder-brand .brand__name { color: #ffffff; font-size: 24px; }
  .folder-brand .brand__mark { width: 14px; height: 14px; }
  .folder-brand__tagline {
    font-size: 8.5px; color: #ffffff; font-weight: 400; margin: 3px 0 0 19px; white-space: nowrap;
  }
  .folder-accent {
    position: absolute; left: 0; top: 300px; width: 90px; height: 110px;
    background: linear-gradient(90deg, rgba(5,14,36,.55), rgba(5,14,36,0));
  }
</style>
</head>
<body>

  <!-- Letterhead, first page -->
  <section class="sheet sheet--letter-first">
    <div class="watermark-area" role="img" aria-label="Grande grafismo decorativo em cinza claro" style="left:0; top:90px; width:150px; height:300px;"></div>
    <div class="brand" style="left:20px; top:16px;">
      <span class="brand__mark"></span>
      <span class="brand__name">PONTE</span>
    </div>
    <span class="brand__tagline" style="left:32px; top:28px;">Gestão com Pessoas</span>
    <div class="header-rule" style="left:78px; right:20px; top:21px;"></div>
    <div class="header-rule header-rule--grey" style="left:20px; right:20px; top:34px;"></div>
    <div class="contact-row" style="bottom:12px;">
      <span class="contact-row__item"><svg viewBox="0 0 10 10"><circle cx="5" cy="5" r="4.3" fill="none" stroke="#3a3d44"/><path d="M3.5 3h1l.5 1.3-.6.5a3 3 0 0 0 1.3 1.3l.5-.6 1.3.5v1a.5.5 0 0 1-.5.5A4 4 0 0 1 3 3.5a.5.5 0 0 1 .5-.5z" fill="#3a3d44"/></svg>(11) 4000-0000</span>
      <span class="contact-row__item"><svg viewBox="0 0 10 10"><circle cx="5" cy="5" r="4.3" fill="none" stroke="#3a3d44"/><path d="M5 2.5a1.7 1.7 0 0 1 1.7 1.7C6.7 5.5 5 7.5 5 7.5S3.3 5.5 3.3 4.2A1.7 1.7 0 0 1 5 2.5z" fill="#3a3d44"/></svg>Rua Central, 100 - Centro</span>
      <span class="contact-row__item"><svg viewBox="0 0 10 10"><circle cx="5" cy="5" r="4.3" fill="none" stroke="#3a3d44"/><rect x="2.8" y="3.4" width="4.4" height="3.2" fill="none" stroke="#3a3d44" stroke-width=".7"/><path d="M2.8 3.4 5 5.2l2.2-1.8" fill="none" stroke="#3a3d44" stroke-width=".7"/></svg>contato@ponte.com</span>
    </div>
    <div class="foot-bar" style="width:70px;"></div>
  </section>

  <!-- Letterhead, continuation page -->
  <section class="sheet sheet--letter-next">
    <div class="watermark-area" role="img" aria-label="Grande grafismo decorativo em cinza claro" style="left:0; top:50px; width:215px; height:360px;"></div>
    <div class="brand" style="left:95px; top:16px;">
      <span class="brand__mark"></span>
      <span class="brand__name">PONTE</span>
    </div>
    <span class="brand__tagline" style="left:107px; top:28px;">Gestão com Pessoas</span>
    <div class="contact-row" style="bottom:14px;">
      <span class="contact-row__item"><svg viewBox="0 0 10 10"><circle cx="5" cy="5" r="4.3" fill="none" stroke="#3a3d44"/><path d="M3.5 3h1l.5 1.3-.6.5a3 3 0 0 0 1.3 1.3l.5-.6 1.3.5v1a.5.5 0 0 1-.5.5A4 4 0 0 1 3 3.5a.5.5 0 0 1 .5-.5z" fill="#3a3d44"/></svg>(11) 4000-0000</span>
      <span class="contact-row__item"><svg viewBox="0 0 10 10"><circle cx="5" cy="5" r="4.3" fill="none" stroke="#3a3d44"/><path d="M5 2.5a1.7 1.7 0 0 1 1.7 1.7C6.7 5.5 5 7.5 5 7.5S3.3 5.5 3.3 4.2A1.7 1.7 0 0 1 5 2.5z" fill="#3a3d44"/></svg>Rua Central, 100 - Centro</span>
      <span class="contact-row__item"><svg viewBox="0 0 10 10"><circle cx="5" cy="5" r="4.3" fill="none" stroke="#3a3d44"/><rect x="2.8" y="3.4" width="4.4" height="3.2" fill="none" stroke="#3a3d44" stroke-width=".7"/><path d="M2.8 3.4 5 5.2l2.2-1.8" fill="none" stroke="#3a3d44" stroke-width=".7"/></svg>contato@ponte.com</span>
    </div>
    <div class="foot-bar" style="width:96px;"></div>
  </section>

  <!-- Presentation folder cover -->
  <section class="sheet sheet--folder">
    <div class="folder-accent" role="img" aria-label="Grafismo decorativo em azul escuro"></div>
    <div class="folder-brand">
      <div class="brand" style="position:static;">
        <span class="brand__mark"></span>
        <span class="brand__name">PONTE</span>
      </div>
      <p class="folder-brand__tagline">Gestão com Pessoas</p>
    </div>
    <div class="foot-bar" style="width:96px;"></div>
  </section>

</body>
</html>
```